MEDICAL CLINIC LETTERHEAD

Design is a letterhead for a non-profit medical center. The name of the clinic is VYRLOTEN Community Health Center. Although the full name must be included, the community health center part is more of a description and should be less visible - i attached an example of what I mean by that (ATTACHED IMAGE IS AN EXAMPLE OF FONT SIZES NOT A DESIGN IDEA). Please design something modern, cool looking and unique because I can always download free templates.
Phone, email, website and etc will be added later.

Industry/Entity Type

MEDICAL

```html
<!DOCTYPE html>
<html lang="en">
<head>
<meta charset="utf-8">
<title>VYRLOTEN Community Health Center — Letterhead</title>
<link href="https://fonts.googleapis.com/css2?family=Lato:wght@400;700&display=swap" rel="stylesheet">
<style>
  :root {
    --brand-blue: #2f74b8;
    --brand-light: #7cc2e6;
    --text-grey: #7a7a7a;
    --footer-text: #3a3a3a;
    --rule: #555555;
    --paper: #ffffff;
  }
  * { margin: 0; padding: 0; box-sizing: border-box; }
  html, body { width: 960px; height: 1200px; overflow: hidden; background: var(--paper); }
  .letterhead {
    position: relative;
    width: 960px;
    height: 1200px;
    background: var(--paper);
    font-family: 'Lato', sans-serif;
  }
  .brand { position: absolute; left: 61px; top: 52px; }
  .brand-mark {
    width: 30px; height: 30px;
    background: var(--brand-blue);
    margin: 0 0 80px 106px;
  }
  .brand-name {
    font-family: 'Lato', sans-serif;
    font-weight: 700;
    font-size: 39px;
    line-height: 1;
    letter-spacing: 0.5px;
    color: var(--brand-blue);
  }
  .brand-descriptor {
    margin-top: 6px;
    font-weight: 700;
    font-size: 16.5px;
    letter-spacing: -0.2px;
    color: var(--brand-light);
  }
  .letter {
    position: absolute;
    left: 60px;
    top: 310px;
    width: 840px;
    color: var(--text-grey);
    font-size: 16.4px;
    line-height: 22px;
  }
  .salutation { margin-left: 20px; margin-bottom: 53px; }
  .letter p { text-align: justify; margin-bottom: 22px; }
  .letter p.opening { text-indent: 55px; }
  .contact-bar {
    position: absolute;
    left: 55px;
    top: 1118px;
    width: 850px;
    height: 54px;
    display: flex;
    color: var(--footer-text);
    font-size: 14.5px;
    line-height: 19px;
  }
  .contact-group { display: flex; align-items: flex-start; }
  .contact-group.address { width: 283px; padding-top: 6px; }
  .contact-group.phones { width: 319px; justify-content: center; padding-top: 0; }
  .contact-group.online { flex: 1; justify-content: flex-end; padding-right: 2px; }
  .divider { width: 1px; height: 52px; background: var(--rule); }
  .contact-list { list-style: none; }
  .contact-list li { display: flex; align-items: center; gap: 10px; height: 19px; margin-bottom: 1px; }
  .icon { width: 12px; height: 12px; flex: none; }
  .pin { width: 12px; height: 18px; margin-right: 8px; margin-top: 2px; flex: none; }
</style>
</head>
<body>
<main class="letterhead">
  <header class="brand">
    <div class="brand-mark" aria-hidden="true"></div>
    <div class="brand-name">VYRLOTEN</div>
    <div class="brand-descriptor">COMMUNITY HEALTH CENTER</div>
  </header>

  <section class="letter">
    <p class="salutation">Dear Sir</p>
    <p class="opening">Lorem ipsum dolor sit amet, consectetur adipiscing elit. Integer eu odio mattis, pulvinar turpis quis, faucibus nisl. Proin feugiat, erat vitae cursus pharetra, enim est semper ligula, in malesuada orci nisl et diam. Etiam elementum metus ac fringilla vulputate. Etiam mattis ligula sed ante mollis bibendum. Orci varius natoque penatibus et magnis dis parturient montes, nascetur ridiculus mus.</p>
    <p>Ut nibh augue, blandit ac orci ac, rutrum congue enim. Suspendisse gravida vulputate felis, quis interdum orci tincidunt quis. Praesent imperdiet maximus neque. Mauris ut dui enim. Nullam at efficitur elit. Donec ante ipsum, fermentum at lectus vel, blandit vulputate ante. Proin luctus suscipit diam id vestibulum. Morbi malesuada id mauris eget ullamcorper.</p>
    <p>Donec varius orci purus, vitae aliquam libero volutpat id. Integer sed imperdiet libero. Aliquam accumsan, risus sit amet ornare consectetur, turpis felis dictum justo, non rhoncus mauris dui sed velit. Pellentesque habitant morbi tristique senectus et netus et malesuada fames ac turpis egestas. Pellentesque tincidunt vitae ligula nec imperdiet. Donec sed congue enim. Nullam elementum faucibus nulla nec vestibulum. Sed at tempor ligula. In quis vulputate nunc. Integer at gravida lacus, ac tristique risus. Sed at vulputate nulla.</p>
    <p>Praesent blandit nunc eu efficitur commodo. In tempor nisi ex, vel venenatis ante vestibulum a. Duis vestibulum nibh a erat sagittis, nec euismod lorem varius. Nam ultricies turpis sed justo sollicitudin volutpat. Morbi sed mollis eros. Sed quis tortor id enim vehicula porttitor. Curabitur non aliquam ex. Phasellus dignissim fermentum elit, at finibus ligula mattis eget.</p>
  </section>

  <footer class="contact-bar">
    <div class="contact-group address">
      <svg class="pin" viewBox="0 0 12 18" aria-hidden="true"><path d="M6 0C2.7 0 0 2.6 0 5.9 0 10 6 18 6 18s6-8 6-12.1C12 2.6 9.3 0 6 0zm0 8.3A2.4 2.4 0 1 1 6 3.5a2.4 2.4 0 0 1 0 4.8z" fill="#444"/></svg>
      <div>suit # 00, Lorem ipsum<br>Lorem Lorem ipsum</div>
    </div>
    <div class="divider"></div>
    <div class="contact-group phones">
      <ul class="contact-list">
        <li><svg class="icon" viewBox="0 0 24 24" aria-hidden="true"><path d="M6.6 10.8a15.1 15.1 0 0 0 6.6 6.6l2.2-2.2c.3-.3.7-.4 1-.2 1.1.4 2.3.6 3.6.6.6 0 1 .4 1 1V20c0 .6-.4 1-1 1A17 17 0 0 1 3 4c0-.6.4-1 1-1h3.5c.6 0 1 .4 1 1 0 1.3.2 2.5.6 3.6.1.3 0 .7-.2 1z" fill="#444"/></svg>000-000-0000</li>
        <li><svg class="icon" viewBox="0 0 24 24" aria-hidden="true"><path d="M6.6 10.8a15.1 15.1 0 0 0 6.6 6.6l2.2-2.2c.3-.3.7-.4 1-.2 1.1.4 2.3.6 3.6.6.6 0 1 .4 1 1V20c0 .6-.4 1-1 1A17 17 0 0 1 3 4c0-.6.4-1 1-1h3.5c.6 0 1 .4 1 1 0 1.3.2 2.5.6 3.6.1.3 0 .7-.2 1z" fill="#444"/></svg>000-000-0000</li>
      </ul>
    </div>
    <div class="divider"></div>
    <div class="contact-group online">
      <ul class="contact-list">
        <li><svg class="icon" viewBox="0 0 24 24" aria-hidden="true"><path d="M2 9l10-6 10 6v11a1 1 0 0 1-1 1H3a1 1 0 0 1-1-1zm3 1.2l7 4.3 7-4.3" fill="#444" stroke="#fff" stroke-width="1.6"/></svg>info@VYRLOTEN.com</li>
        <li><svg class="icon" viewBox="0 0 24 24" aria-hidden="true"><g fill="none" stroke="#444" stroke-width="2"><circle cx="12" cy="12" r="10"/><ellipse cx="12" cy="12" rx="4.5" ry="10"/><path d="M2 12h20M4 7h16M4 17h16"/></g></svg>www.VYRLOTEN.com</li>
      </ul>
    </div>
  </footer>
</main>
</body>
</html>
```